Nobre Lente Lusitana - business card

Create a business card for my eyewear (glasses) store. The concept is based in handcrafted glasses (as well as common frames and 3d printed), clean, and elegant. The business card could be black (white letters and symbols) or white (black letters and symbols) but we are open to new suggestions. It must be sober and elegant.
The name Nobre Lente Lusitana means Royal/Real Portuguese Optical Store.
Our concept should be inspired by the pictures attatched bellow.
I would like it to be classic and elegant as business cards for bankers.
Our first selected logo is also available in attachment files.

Target Market(s)

For business meetings with investors, supliers and fairs

Industry/Entity Type

Eyewear

Contact Information for Business Card

Some random business cards in attachment that we like. Don't be closed to it, we like freedom of think.

Font styles to use
Serif
Sans Serif

Colors
404040
e9e9e9
fbfbfb
000000
85abd3
0255a3
f7fbfd
959595

Requirements
Must have
• Must be elegant, simple.
• Must present our brand new logo (slight variations are welcome, the logo is not closed yet). See our temporary logo in attachment.
• Black (or dark grey), white (or light grey) and a third slight color.
• This third slight color could be dark blue or grayish blue.
• Info:
• Tomás Vidigal (name)
• tvidigal@nobrelentelusitana.example
• +351 927364051
• www.nobrelentelusitana.example
Nice to have
• Black and white or with serious colors such as dark blue or greyish blue.
• Could also have water mark with our logo (big size) in the background (inspired in KMT bank credit card design)
Should not have
• Hysteric colora or shapes

```html
<!DOCTYPE html>
<html lang="pt">
<head>
<meta charset="utf-8">
<title>Nobre Lente Lusitana — Cartão de visita</title>
<link href="https://fonts.googleapis.com/css2?family=Cinzel:wght@400;500&family=Montserrat:wght@400&display=swap" rel="stylesheet">
<style>
  :root{
    --ink:#000000;
    --ink-soft:#404040;
    --paper:#fbfbfb;
    --backdrop:#e9e9e9;
    --rule:#959595;
    --ornament:#cfcfcf;
  }
  *{box-sizing:border-box;margin:0;padding:0}
  html,body{width:1200px;height:720px;overflow:hidden}
  body{background:var(--backdrop);font-family:'Montserrat',sans-serif;color:var(--ink)}
  .stage{position:relative;width:1200px;height:720px}
  .card{position:absolute;top:210px;width:520px;height:300px;background:var(--paper);
        border-bottom:3px solid var(--ink);box-shadow:0 2px 6px rgba(0,0,0,.12)}
  .card--front{left:50px}
  .card--back{left:630px}

  .front-frame{position:absolute;inset:10px;border:1.5px solid var(--ink);display:flex}
  .brand-panel{width:170px;border-right:1px solid var(--ink-soft);margin:18px 0;
        display:flex;align-items:center;justify-content:center;gap:7px}
  .brand-mark{width:7px;height:7px;border-radius:50%;background:var(--ink-soft);flex:none}
  .brand-name{font-family:'Montserrat',sans-serif;font-weight:400;font-size:11px;
        white-space:nowrap;color:var(--ink-soft)}

  .identity-panel{flex:1;padding:34px 24px 0 30px;display:flex;flex-direction:column;align-items:center}
  .holder{display:flex;align-items:center;gap:8px;width:100%;justify-content:center}
  .holder-rule{flex:1;height:1px;background:var(--ink);position:relative}
  .holder-rule::after{content:"";position:absolute;top:-2px;width:5px;height:5px;border-radius:50%;background:var(--ink)}
  .holder-rule--left::after{left:0}
  .holder-rule--right::after{right:0}
  .holder-name{font-family:'Cinzel',serif;font-size:24px;font-weight:500;letter-spacing:1px;color:var(--ink);white-space:nowrap}
  .flourish{width:150px;height:22px;margin-top:6px;border-radius:11px;background:var(--ornament)}

  .contact-list{list-style:none;margin-top:34px;align-self:flex-start;display:flex;flex-direction:column;gap:6px}
  .contact-item{display:flex;align-items:center;gap:10px;font-size:11px;color:var(--ink-soft)}
  .contact-icon{width:12px;height:12px;flex:none}

  .back-content{position:absolute;inset:0;display:flex;align-items:center;justify-content:center;gap:10px}
  .back-content .brand-mark{width:10px;height:10px}
  .back-content .brand-name{font-size:18px}
  .back-url{position:absolute;bottom:34px;left:0;right:0;text-align:center;font-size:11px;color:var(--ink-soft)}
</style>
</head>
<body>
<main class="stage">
  <section class="card card--front" aria-label="Frente do cartão">
    <div class="front-frame">
      <div class="brand-panel">
        <span class="brand-mark"></span>
        <p class="brand-name">Nobre Lente Lusitana</p>
      </div>
      <div class="identity-panel">
        <div class="holder">
          <span class="holder-rule holder-rule--left"></span>
          <h1 class="holder-name">Tomás Vidigal</h1>
          <span class="holder-rule holder-rule--right"></span>
        </div>
        <div class="flourish" role="img" aria-label="Ornamento clássico em arabesco sob o nome"></div>
        <ul class="contact-list">
          <li class="contact-item">
            <svg class="contact-icon" viewBox="0 0 24 24"><path fill="#404040" d="M6.6 10.8a15 15 0 0 0 6.6 6.6l2.2-2.2a1 1 0 0 1 1-.25 11.4 11.4 0 0 0 3.6.57 1 1 0 0 1 1 1V20a1 1 0 0 1-1 1A17 17 0 0 1 3 4a1 1 0 0 1 1-1h3.5a1 1 0 0 1 1 1c0 1.250.2 2.450.57 3.57a1 1 0 0 1-.25 1z"/></svg>
            +351 927364051
          </li>
          <li class="contact-item">
            <svg class="contact-icon" viewBox="0 0 24 24"><rect x="2" y="5" width="20" height="14" rx="1" fill="#404040"/><path d="M3 6l9 7 9-7" stroke="#fbfbfb" stroke-width="1.6" fill="none"/></svg>
            tvidigal@nobrelentelusitana.example
          </li>
          <li class="contact-item">
            <svg class="contact-icon" viewBox="0 0 24 24"><circle cx="12" cy="12" r="10" fill="#404040"/><path d="M2 12h20M12 2c3 3 3 17 0 20M12 2c-3 3-3 17 0 20" stroke="#fbfbfb" stroke-width="1.2" fill="none"/></svg>
            www.nobrelentelusitana.example
          </li>
        </ul>
      </div>
    </div>
  </section>

  <section class="card card--back" aria-label="Verso do cartão">
    <div class="back-content">
      <span class="brand-mark"></span>
      <p class="brand-name">Nobre Lente Lusitana</p>
    </div>
    <p class="back-url">www.nobrelentelusitana.example</p>
  </section>
</main>
</body>
</html>
```